Website Design for a DJ Entertainment and Productions Comany

We are a full service DJ Entertainment and Productions company looking to have a strong presence in our local market and need a phenomenal website design to drive clients to the site but then also keep them there. We cater to all types of different events varying from weddings to proms to corporate events, birthdays, bar mitzvah's and so on and so on. We also do full lighting for any type of event and we also offer a photobooth service for various events. The best way to get an idea of the services that we offer is to visit http://www.velvarmusicworks.com/index.html This site is NOT our own but only linked as an example of what we do and will give you an overall overview of what we offer.
We are looking for pure creativity as there are multiple facets to our company and the services we offer. On the one hand we can provide a night club party atmosphere for Proms or dances but on the other hand we also provide professional full service emcee/DJ for weddings and formal events. The key for this site would be to have the pages for each category match the look and feel of the actual service provided, ie the Wedding page will look more refined and professional vs the Party DJ page. Each page needs to fit the overall feel of the Company and Logo though. Here is a list of pages that we would need to have on the final site.
HOME PAGE
PROFESSINAL DJS- This will have info. and pricing of our DJ services for everything but weddings. Should have pics and videos somewhere on this page.
WEDDINGS- All wedding package pricing and info. This page should look more elegant, formal and high class compared to the other pages.
PHOTOBOOTH-Page with info, pricing on photobooth see http://www.glimmerboxkiosk.com/
LIGHTING DESIGN-Info on our lighting services along with pricing
CORPORATE EVENTS-Info on services and pricing for corporate events. This page should seem more professional centered towards business clientele.
CLIENT LOGIN-Page for existing clients to logon to update info and fill out information.
CONNECT WITH US- Social Media links.
Our logo was submitted through Pixel Forum but I am open to suggestions on revisions if you feel the need to change it. Color is also not set in stone.
Updates
I have increased my budget $200 more. Please submit your designs for review, deadline is approaching quickly. Also see brief for revisions.
Thank you.
Target Market(s)
Broad Range but usually Under 40
Industry/Entity Type
Night Club
Look and feel

```html
<!DOCTYPE html>
<html lang="en">
<head>
<meta charset="utf-8">
<title>Lumen Entertainment &amp; Productions — Photobooth</title>
<link href="https://fonts.googleapis.com/css2?family=Montserrat:wght@400;500;600;700&display=swap" rel="stylesheet">
<style>
:root{
  --ink:#0b0308;
  --plum:#3a0b2c;
  --hot:#ff4c9f;
  --pink-tag:#ff5aa5;
  --red:#e8232f;
  --white:#ffffff;
  --frame:#f6f3f4;
}
*{margin:0;padding:0;box-sizing:border-box}
html,body{width:1200px;height:744px;overflow:hidden;background:var(--ink)}
body{font-family:"Montserrat",Arial,sans-serif;color:var(--white);position:relative}
.site-header{position:absolute;left:0;top:0;width:1200px;height:122px;
  background:radial-gradient(ellipse 560px 170px at 330px 50px,#4e1038 0%,#22061a 60%,var(--ink) 100%)}
.brand{position:absolute;left:246px;top:14px;display:flex;align-items:center;gap:10px}
.brand-mark{width:54px;height:54px;border-radius:50%;background:var(--red)}
.brand-name{display:block;font-weight:700;font-size:32px;letter-spacing:2px;color:var(--red);line-height:1}
.brand-sub{display:block;font-size:7px;font-weight:700;letter-spacing:.2px;color:var(--red);margin-top:3px}
.login{position:absolute;right:155px;top:39px;font-weight:700;font-size:14px;color:var(--red);text-decoration:none}
.main-nav{position:absolute;left:246px;top:93px;width:800px;display:flex;justify-content:space-between}
.main-nav a{font-size:12.5px;color:var(--white);text-decoration:none;letter-spacing:.2px}
.main-nav a.is-active{color:var(--red)}
.hero{position:absolute;left:0;top:122px;width:1200px;height:519px;overflow:hidden;
  background:radial-gradient(ellipse 430px 400px at 330px 440px,var(--hot) 0%,#cf2f80 28%,#7a1658 58%,var(--plum) 82%,#1a0514 100%)}
.collage{position:absolute;left:0;top:0}
.product{position:absolute;left:250px;top:66px}
.product-name{font-size:42px;font-weight:500;color:var(--white);line-height:1;letter-spacing:.5px}
.product-tag{font-size:15px;color:var(--pink-tag);margin-left:94px;margin-top:1px;font-weight:500}
.intro{position:absolute;left:242px;top:148px;width:375px;font-size:11px;line-height:16px}
.intro p{margin-bottom:16px}
.contact{position:absolute;left:240px;top:367px;font-size:11px;line-height:17px}
.contact a{color:var(--white);text-decoration:none;font-size:12.5px;letter-spacing:.2px}
.slide{position:absolute;left:646px;top:143px;width:396px;height:241px;overflow:hidden;
  background:
    radial-gradient(ellipse 120px 90px at 170px 150px,#d9a58a 0%,rgba(217,165,138,.55) 40%,rgba(217,165,138,0) 100%),
    radial-gradient(ellipse 90px 70px at 260px 120px,#c9c4cc 0%,rgba(201,196,204,.4) 45%,rgba(201,196,204,0) 100%),
    linear-gradient(90deg,#7a1626 0%,#4a0f1b 30%,#2a0c12 60%,#555 85%,#1b1b1b 100%)}
.dots{position:absolute;left:829px;top:404px;display:flex;gap:4px}
.dots span{width:8px;height:8px;border-radius:50%;background:#8d8d8d}
.dots span.is-current{background:var(--red)}
.site-footer{position:absolute;left:0;top:641px;width:1200px;height:103px;
  background:radial-gradient(ellipse 440px 120px at 420px 104px,#520e3b 0%,#1c0515 60%,var(--ink) 100%);
  border-top:2px solid #120410}
.book{position:absolute;left:240px;top:15px;font-size:19.5px;letter-spacing:.3px}
.book .label{color:var(--red)}
.copyright{position:absolute;left:240px;top:49px;font-size:9.5px;letter-spacing:.2px}
.follow{position:absolute;left:893px;top:17px;display:flex;align-items:center;gap:8px;font-weight:700;font-size:12.5px;letter-spacing:.5px}
.social{width:24px;height:24px;border-radius:4px;display:inline-block}
.social.one{background:#2f5b9c;margin-left:2px}
.social.two{background:#4fb8e6}
</style>
</head>
<body>
<header class="site-header">
  <div class="brand">
    <span class="brand-mark"></span>
    <div><span class="brand-name">LUMEN</span><span class="brand-sub">ENTERTAINMENT &amp; PRODUCTIONS</span></div>
  </div>
  <a class="login" href="#">Login</a>
  <nav class="main-nav">
    <a href="#">PROFESSIONAL DJS</a>
    <a href="#">WEDDINGS</a>
    <a href="#">PHOTOBOOTH</a>
    <a href="#">LIGHTING DESIGN</a>
    <a href="#" class="is-active">CORPORATE EVENTS</a>
    <a href="#">EVENT DESIGN</a>
  </nav>
</header>

<section class="hero">
  <svg class="collage" width="1200" height="519" viewBox="0 0 1200 519" role="img" aria-label="Collage of tilted photobooth snapshots: guests posing, the booth start button, the booth cabinet and red curtains">
    <defs>
      <linearGradient id="curtain" x1="0" y1="0" x2="1" y2="0">
        <stop offset="0" stop-color="#8e1a2c"/><stop offset=".5" stop-color="#c2313f"/><stop offset="1" stop-color="#5a0d1a"/>
      </linearGradient>
      <radialGradient id="guests" cx=".45" cy=".5" r=".7">
        <stop offset="0" stop-color="#c48a6c"/><stop offset=".45" stop-color="#6b2a26"/><stop offset="1" stop-color="#1d0a0c"/>
      </radialGradient>
      <radialGradient id="button" cx=".45" cy=".55" r=".6">
        <stop offset="0" stop-color="#3fb6f0"/><stop offset=".25" stop-color="#14597f"/><stop offset=".55" stop-color="#0e0e10"/><stop offset="1" stop-color="#2b2b2e"/>
      </radialGradient>
      <linearGradient id="booth" x1="0" y1="0" x2="1" y2="1">
        <stop offset="0" stop-color="#a3161f"/><stop offset=".4" stop-color="#c9c9cc"/><stop offset=".75" stop-color="#6d6d70"/><stop offset="1" stop-color="#d9b98a"/>
      </linearGradient>
      <linearGradient id="warm" x1="0" y1="0" x2="1" y2="1">
        <stop offset="0" stop-color="#3a1a10"/><stop offset=".5" stop-color="#b4603a"/><stop offset="1" stop-color="#2a0e0a"/>
      </linearGradient>
      <linearGradient id="night" x1="0" y1="0" x2="1" y2="1">
        <stop offset="0" stop-color="#4a3a36"/><stop offset=".5" stop-color="#8a6a5a"/><stop offset="1" stop-color="#1a1010"/>
      </linearGradient>
      <linearGradient id="silver" x1="0" y1="0" x2="1" y2="0">
        <stop offset="0" stop-color="#2a2a2c"/><stop offset=".5" stop-color="#bdbdc0"/><stop offset="1" stop-color="#4a4a4d"/>
      </linearGradient>
      <clipPath id="leftStrip"><polygon points="0,0 248,0 52,519 0,519"/></clipPath>
      <clipPath id="rightStrip"><polygon points="680,0 1150,0 1184,519 594,519 700,384 770,143"/></clipPath>
    </defs>

    <polygon points="0,0 248,0 52,519 0,519" fill="var(--frame)"/>
    <g clip-path="url(#leftStrip)" stroke="var(--frame)" stroke-width="8">
      <rect x="62" y="-38" width="190" height="110" fill="url(#curtain)" transform="rotate(24 157 17)"/>
      <rect x="17" y="38" width="190" height="112" fill="url(#button)" transform="rotate(24 112 94)"/>
      <rect x="-15" y="142" width="190" height="112" fill="url(#booth)" transform="rotate(24 80 198)"/>
      <rect x="-39" y="246" width="190" height="112" fill="url(#guests)" transform="rotate(24 56 302)"/>
      <rect x="-63" y="350" width="190" height="112" fill="url(#warm)" transform="rotate(24 32 406)"/>
      <rect x="-79" y="440" width="190" height="112" fill="url(#curtain)" transform="rotate(24 16 494)"/>
    </g>

    <polygon points="680,0 1150,0 1184,519 594,519 700,384 770,143" fill="var(--frame)"/>
    <g clip-path="url(#rightStrip)" stroke="var(--frame)" stroke-width="8">
      <rect x="700" y="-10" width="110" height="40" fill="url(#night)" transform="rotate(-30 755 10)"/>
      <rect x="716" y="2" width="200" height="120" fill="url(#booth)" transform="rotate(-30 816 62)"/>
      <rect x="916" y="10" width="200" height="120" fill="url(#guests)" transform="rotate(-30 1016 70)"/>
      <rect x="880" y="80" width="170" height="90" fill="url(#warm)" transform="rotate(-30 965 125)"/>
      <rect x="1080" y="-30" width="110" height="70" fill="url(#silver)" transform="rotate(-30 1135 5)"/>
      <rect x="1004" y="290" width="200" height="130" fill="url(#warm)" transform="rotate(-30 1104 355)"/>
      <rect x="652" y="378" width="200" height="120" fill="url(#guests)" transform="rotate(-30 752 438)"/>
      <rect x="620" y="446" width="200" height="110" fill="url(#night)" transform="rotate(-30 720 501)"/>
      <rect x="932" y="394" width="200" height="120" fill="url(#silver)" transform="rotate(-30 1032 454)"/>
      <rect x="830" y="460" width="180" height="100" fill="url(#curtain)" transform="rotate(-30 920 510)"/>
      <rect x="1090" y="450" width="140" height="100" fill="url(#warm)" transform="rotate(-30 1160 500)"/>
    </g>
  </svg>

  <div class="product">
    <div class="product-name">Glimmerbox</div>
    <div class="product-tag">photobooth rentals</div>
  </div>

  <div class="intro">
    <p>The party everyone will talk about, we're talking about yours. Velvar Party DJs provides modern DJs in Michigan for big and small events. You deserve more than just music, so we will give you fun options that will keep your dance floor packed. Log online and drag and drop songs with your online party planner.</p>
    <p>Your guests get Tap n Queue access so they can request songs months in advance. And how cool is it for them to download photos from your Shine Cam Photo Album. Share the fun and experience the difference, you will get more value with our unique options. Do you want more information about a Fun Michigan DJ company? Please click the logo below and take your first step towards the best event ever.</p>
  </div>

  <div class="contact">
    Feel free to contact us to book a consultation.<br>
    <a href="#">DJS@LUMENSTAGEWORKS.COM</a>
  </div>

  <div class="slide" role="img" aria-label="Slideshow photo of friends posing together inside the photobooth in front of a red curtain"></div>
  <div class="dots"><span></span><span></span><span class="is-current"></span><span></span><span></span></div>
</section>

<footer class="site-footer">
  <div class="book"><span class="label">BOOK NOW</span> 917.555.0142</div>
  <div class="copyright">© 2011 LUMEN ENTERTAINMENT &amp; PRODUCTIONS</div>
  <div class="follow">FOLLOW US: <span class="social one"></span><span class="social two"></span></div>
</footer>
</body>
</html>
```